RW Hollis LLC Business Card - Civil Engineering & Consulting Firm

We need a Business Card that is elegant, and masculine.  It is our Professional Civil Engineering & Consulting Company located in San Antonio TX (Not s construction or builder firm- no gears & no tool images please). We provide civil engineering services including  commercial site plans, grading and drainage plans, utility plans, hydraulics and hydrology, land planning, utility coordination, and other general civil engineering services related to commercial and residential development.
We have 2 existing Logos. We would like to convey reliability, strength, trustworthiness and attention to detail.  Blues and orange tones as per logo We are OK with the use of a darker blue in the mix.  We have 2 logo versions - Full Company Name Logo to go on the back of card, & Small Icon Logo for the front w/ personal Info.

Target Market(s)
Architects, Real Estate Developers, Other Strctural Engineers, Surveyers, General Contractors
Industry/Entity Type
Professional Civil Engineering
Contact Information for Business Card
Name, Position, Address, Cell & Office #, email, and company website
Font styles to use
Other font styles liked:
- Avian
Requirements
Should not have
- No Tools, No Gears, no Cranes, or Construction Equipment.

```html
<!DOCTYPE html>
<html lang="en">
<head>
<meta charset="utf-8">
<title>RW Hollis LLC – Business Card</title>
<link href="https://fonts.googleapis.com/css2?family=Questrial&family=Montserrat:wght@700&display=swap" rel="stylesheet">
<style>
  :root {
    --page: #e7e9ee;
    --card-white: #f5f6f9;
    --navy: #34508f;
    --sky: #77acd8;
    --orange: #f0912a;
    --text-light: #ffffff;
  }
  * { margin: 0; padding: 0; box-sizing: border-box; }
  html, body { width: 1200px; height: 1021px; overflow: hidden; }
  body {
    background: var(--page);
    font-family: "Questrial", "Century Gothic", sans-serif;
    position: relative;
  }
  .card {
    position: absolute;
    left: 220px;
    width: 760px;
    height: 434px;
    border-radius: 4px;
    overflow: hidden;
    box-shadow: 0 8px 24px rgba(20, 30, 60, 0.18);
  }

  /* Company name: one colour, one weight */
  .company-name {
    color: var(--sky);
    font-family: "Questrial", "Century Gothic", sans-serif;
    font-weight: 400;
    letter-spacing: 0.08em;
    line-height: 1;
    white-space: nowrap;
  }

  /* Front: personal details */
  .card--front { top: 51px; background: var(--navy); }
  .front__header {
    position: absolute; left: 0; top: 0; width: 100%; height: 150px;
    background: var(--card-white);
    border-bottom: 4px solid var(--sky);
    display: flex; align-items: center; justify-content: center;
  }
  .front__header .company-name { font-size: 44px; }

  .person { position: absolute; left: 60px; top: 290px; }
  .person__name {
    font-family: "Montserrat", "Arial", sans-serif;
    font-weight: 700; font-size: 38px; color: var(--orange); line-height: 1;
    white-space: nowrap;
  }
  .person__role {
    font-size: 15px; color: var(--text-light); letter-spacing: 0.06em; margin-top: 6px;
    padding-bottom: 8px; border-bottom: 2px solid var(--text-light); display: inline-block; width: 110px;
  }

  .contacts { position: absolute; left: 420px; top: 190px; list-style: none; }
  .contacts li { display: flex; align-items: center; gap: 16px; margin-bottom: 24px; }
  .contacts svg { width: 34px; height: 34px; flex: none; }
  .contacts p { color: var(--text-light); font-size: 17px; line-height: 1.25; white-space: nowrap; }

  /* Back: company name only */
  .card--back {
    top: 536px; background: var(--card-white);
    display: flex; align-items: center; justify-content: center;
  }
  .card--back .company-name { font-size: 72px; }
</style>
</head>
<body>

  <section class="card card--front" aria-label="Business card front">
    <header class="front__header">
      <div class="company-name">RW Hollis LLC</div>
    </header>

    <div class="person">
      <div class="person__name">Dale MORROW</div>
      <div class="person__role">ENGINEER</div>
    </div>

    <ul class="contacts">
      <li>
        <svg viewBox="0 0 34 34" aria-hidden="true" fill="none" stroke="#f0912a" stroke-width="2">
          <circle cx="17" cy="17" r="14"/>
          <path d="M12 10c-2 2 0 7 4 10s7 4 8 2l1-2-3-2-2 1c-2-1-4-3-5-5l1-2-2-3z"/>
        </svg>
        <p>+(000) 812.330.417<br>+(000) 812.330.452</p>
      </li>
      <li>
        <svg viewBox="0 0 34 34" aria-hidden="true" fill="none" stroke="#f0912a" stroke-width="2">
          <path d="M17 31s-10-10-10-17a10 10 0 0 1 20 0c0 7-10 17-10 17z"/>
          <circle cx="17" cy="14" r="4"/>
        </svg>
        <p>info@rwhollis.com<br>www.rwhollis.com</p>
      </li>
      <li>
        <svg viewBox="0 0 34 34" aria-hidden="true" fill="none" stroke="#f0912a" stroke-width="2">
          <circle cx="17" cy="17" r="14"/>
          <ellipse cx="17" cy="17" rx="6" ry="14"/>
          <path d="M3 17h28M6 10h22M6 24h22"/>
        </svg>
        <p>402, Brookline,<br>Texas, USA.</p>
      </li>
    </ul>
  </section>

  <section class="card card--back" aria-label="Business card back">
    <div class="company-name">RW Hollis LLC</div>
  </section>

</body>
</html>
```